Urine collection cup with and without sterile seal sticker

Hello. We need a urine cup label designed please with

Name:
Date of Birth:
Date:
Time:
Temp℃:
Specimen ID:

Product code: TUB-47
Volume markings (e.g., 30 mL, 60 mL, 90 mL).
Vela Drug Tests logo

Could you please provide one version with the additional sterile sticker extending to the top, and one version without the additional sterile sticker?

```html
<!DOCTYPE html>
<html lang="en">
<head>
<meta charset="utf-8">
<title>Vela Drug Tests – Collection Cup Labels</title>
<link href="https://fonts.googleapis.com/css2?family=Montserrat:wght@500;700&family=Oswald:wght@500;600&family=Roboto+Condensed:wght@500&display=swap" rel="stylesheet">
<style>
  :root {
    --navy: #263570;
    --sky: #1fb3e8;
    --paper: #ffffff;
    --canvas: #ffffff;
    --ink: #263570;
    --caption: #111111;
  }
  * { box-sizing: border-box; margin: 0; padding: 0; }
  html, body { width: 1200px; height: 501px; overflow: hidden; background: var(--canvas); }
  .stage { position: relative; width: 1200px; height: 501px; }

  .label {
    position: absolute;
    top: 175px;
    width: 314px;
    height: 251px;
    background: var(--paper);
    box-shadow: 0 4px 14px rgba(0,0,0,0.18);
  }
  .label--sealed { left: 468px; }
  .label--plain { left: 828px; }

  .label__band {
    position: absolute; left: 0; top: 0; right: 0; height: 66px;
    background: var(--navy);
  }
  .brand-name {
    position: absolute; left: 24px; top: 20px;
    font: 700 24px/1 "Montserrat", sans-serif;
    color: var(--paper);
    letter-spacing: 0.2px;
  }

  .volume-scale { position: absolute; left: 12px; top: 80px; width: 40px; height: 120px; }
  .volume-scale text { font: 500 6px "Roboto Condensed", sans-serif; fill: var(--ink); }

  .fields { position: absolute; left: 56px; top: 75px; list-style: none; }
  .field {
    display: flex; align-items: flex-end;
    height: 22px;
    font: 500 14px/1 "Roboto Condensed", sans-serif;
    color: var(--ink);
    white-space: nowrap;
  }
  .field__line { flex: 1; border-bottom: 1px solid var(--ink); margin-left: 4px; margin-bottom: 2px; }
  .label--sealed .fields { width: 174px; }
  .label--plain .fields { width: 238px; }

  .product-code {
    position: absolute; left: 13px; top: 221px;
    height: 18px; padding: 0 5px;
    background: var(--navy); color: var(--paper);
    border-radius: 2px;
    font: 500 13px/18px "Roboto Condensed", sans-serif;
  }

  .seal {
    position: absolute; left: 698px; top: 70px;
    width: 84px; height: 356px;
    background: var(--navy);
  }
  .seal__title {
    position: absolute; left: 50%; top: 26px; transform: translateX(-50%);
    writing-mode: vertical-rl;
    font: 600 37px/1 "Oswald", sans-serif;
    color: var(--paper);
    letter-spacing: 1px;
  }
  .seal__note {
    position: absolute; left: 50%; top: 196px; transform: translateX(-50%);
    writing-mode: vertical-rl;
    font: 700 13px/17px "Montserrat", sans-serif;
    color: var(--sky);
    text-align: center;
  }

  .caption {
    position: absolute; top: 445px; width: 260px; text-align: center;
    font: 500 17px/1 "Montserrat", sans-serif;
    color: var(--caption);
  }
  .caption--sealed { left: 498px; }
  .caption--plain { left: 854px; }
</style>
</head>
<body>
<main class="stage">

  <!-- Label with sterile seal -->
  <section class="label label--sealed">
    <div class="label__band"><span class="brand-name">Vela Drug Tests</span></div>
    <svg class="volume-scale" viewBox="0 0 40 120" aria-hidden="true">
      <g stroke="var(--ink)" stroke-width="1">
        <line x1="3" y1="3" x2="3" y2="115"/>
        <line x1="3" y1="3" x2="12" y2="3"/>
        <line x1="3" y1="59" x2="12" y2="59"/>
        <line x1="3" y1="115" x2="12" y2="115"/>
        <path d="M3 10h4M3 17h4M3 24h4M3 31h4M3 38h4M3 45h4M3 52h4M3 66h4M3 73h4M3 80h4M3 87h4M3 94h4M3 101h4M3 108h4"/>
      </g>
      <text x="15" y="5">90 ml</text>
      <text x="15" y="61">60 ml</text>
      <text x="15" y="117">30 ml</text>
    </svg>
    <ul class="fields">
      <li class="field">Name:<span class="field__line"></span></li>
      <li class="field">Date of Birth:<span class="field__line"></span></li>
      <li class="field">Date:<span class="field__line"></span></li>
      <li class="field">Time:<span class="field__line"></span></li>
      <li class="field">Temp°C:<span class="field__line"></span></li>
      <li class="field">Specimen ID:<span class="field__line"></span></li>
    </ul>
    <div class="product-code">Product code: TUB-47</div>
  </section>
  <aside class="seal">
    <span class="seal__title">STERILE</span>
    <span class="seal__note">TIGHTEN CAP<br>SECURELY</span>
  </aside>
  <p class="caption caption--sealed">With Sterile Seal</p>

  <!-- Label without sterile seal -->
  <section class="label label--plain">
    <div class="label__band"><span class="brand-name">Vela Drug Tests</span></div>
    <svg class="volume-scale" viewBox="0 0 40 120" aria-hidden="true">
      <g stroke="var(--ink)" stroke-width="1">
        <line x1="3" y1="3" x2="3" y2="115"/>
        <line x1="3" y1="3" x2="12" y2="3"/>
        <line x1="3" y1="59" x2="12" y2="59"/>
        <line x1="3" y1="115" x2="12" y2="115"/>
        <path d="M3 10h4M3 17h4M3 24h4M3 31h4M3 38h4M3 45h4M3 52h4M3 66h4M3 73h4M3 80h4M3 87h4M3 94h4M3 101h4M3 108h4"/>
      </g>
      <text x="15" y="5">90 ml</text>
      <text x="15" y="61">60 ml</text>
      <text x="15" y="117">30 ml</text>
    </svg>
    <ul class="fields">
      <li class="field">Name:<span class="field__line"></span></li>
      <li class="field">Date of Birth:<span class="field__line"></span></li>
      <li class="field">Date:<span class="field__line"></span></li>
      <li class="field">Time:<span class="field__line"></span></li>
      <li class="field">Temp°C:<span class="field__line"></span></li>
      <li class="field">Specimen ID:<span class="field__line"></span></li>
    </ul>
    <div class="product-code">Product code: TUB-47</div>
  </section>
  <p class="caption caption--plain">Without Sterile Seal</p>

</main>
</body>
</html>
```